KIVO Cosmetics LABELS

one good design wanted for the KIVO COSMETICS brand.

These are cosmetics and detergents. The labels should be about 3" wide and 4" deep. It must be colorful and interesting with some art on it. Flowers, girl, ? anything.

The word KIVO should guide your thinking a little.

It has to be bold and with striking colors. The attached images are there only as a guide of images we like and the logos are there, so you can see what we have already.

Ask any further questions please.

This design should be colorful and not finicky

Reason: Ready to work with any designer - through Brief Harbor - for other projects.

some intriguing graphics, images or something 'wow' is wanted in the designs

Those wanting something different and economic.

Cosmetics

• Each label in a range is to be the same 'ish and to allow space for the name of the individual product to be added; such as Seaweed Shampoo.

Use of the logo will be all labels but small in a corner, or ...

USE OF THE SHOWN IMAGES, SHOULD BE THERE BUT NOT PROMINENTLY

```html
<!DOCTYPE html>
<html lang="en">
<head>
<meta charset="utf-8">
<title>KIVO Cosmetics – Shimmer Lotion Label</title>
<link rel="stylesheet" href="https://fonts.googleapis.com/css2?family=Pacifico&family=Saira+Condensed:wght@500;700&display=swap">
<style>
  :root {
    --label-black: #030405;
    --ink-white: #ffffff;
    --ink-grey: #8a8b8d;
    --brand-blue: #2aa9e0;
    --accent-pink: #d0197a;
    --ornament-blue: #1f9fd8;
    --ornament-purple: #5a2d8c;
    --ornament-pink: #d8197c;
  }
  html, body {
    margin: 0;
    padding: 0;
    overflow: hidden;
    background: var(--label-black);
  }
  .label {
    position: relative;
    width: 680px;
    height: 1200px;
    background: var(--label-black);
    overflow: hidden;
  }
  .label__art {
    position: absolute;
    inset: 0;
    width: 680px;
    height: 1200px;
  }
  .brand-name {
    position: absolute;
    left: 172px;
    top: 336px;
    margin: 0;
    font-family: "Saira Condensed", sans-serif;
    font-weight: 500;
    font-size: 48px;
    line-height: 1;
    color: var(--brand-blue);
    letter-spacing: 1px;
  }
  .product-block {
    position: absolute;
    right: 71px;
    top: 748px;
    text-align: right;
  }
  .product-block__tagline {
    margin: 0 0 4px;
    font-family: "Pacifico", cursive;
    font-size: 50px;
    line-height: 1.1;
    color: var(--ink-white);
  }
  .product-block__name {
    margin: 0;
    font-family: "Saira Condensed", sans-serif;
    font-weight: 700;
    font-size: 70px;
    line-height: 0.96;
    letter-spacing: 1px;
    color: var(--ink-grey);
    text-transform: uppercase;
  }
  .net-content {
    position: absolute;
    left: 30px;
    bottom: 22px;
    margin: 0;
    font-family: "Saira Condensed", sans-serif;
    font-weight: 700;
    font-size: 46px;
    line-height: 1;
    color: var(--ink-white);
  }
</style>
</head>
<body>
<main class="label">
  <svg class="label__art" viewBox="0 0 680 1200" xmlns="http://www.w3.org/2000/svg">
    <defs>
      <linearGradient id="ornament-top-tone" x1="0" y1="0" x2="1" y2="0">
        <stop offset="0" stop-color="var(--ornament-blue)" stop-opacity="0.55"/>
        <stop offset="0.55" stop-color="var(--ornament-purple)" stop-opacity="0.55"/>
        <stop offset="1" stop-color="var(--ornament-pink)" stop-opacity="0.55"/>
      </linearGradient>
      <linearGradient id="ornament-bottom-tone" x1="0" y1="0" x2="1" y2="0">
        <stop offset="0" stop-color="var(--ornament-pink)" stop-opacity="0.55"/>
        <stop offset="0.6" stop-color="var(--ornament-purple)" stop-opacity="0.5"/>
        <stop offset="1" stop-color="var(--ornament-pink)" stop-opacity="0.55"/>
      </linearGradient>
    </defs>

    <path class="ornament ornament--top" role="img"
          aria-label="Henna-style paisley and mandala line ornament in blue, purple and pink"
          fill="url(#ornament-top-tone)"
          d="M50 290 C40 220 70 150 130 115 C190 90 260 100 300 150 C330 130 370 120 400 140 C450 110 540 150 600 190 C625 220 622 265 612 295 Z"/>

    <path class="ornament ornament--bottom" role="img"
          aria-label="Henna-style mandala line ornament in pink and blue"
          fill="url(#ornament-bottom-tone)"
          d="M112 445 L532 440 C540 490 520 540 470 570 C430 600 380 605 345 595 C320 620 300 634 285 632 C240 625 170 600 135 560 C110 530 105 480 112 445 Z"/>

    <path class="divider divider--top" fill="none" stroke="var(--accent-pink)" stroke-width="3" stroke-linecap="round"
          d="M50 292 Q330 308 617 300"/>
    <path class="divider divider--bottom" fill="none" stroke="var(--accent-pink)" stroke-width="3" stroke-linecap="round"
          d="M62 450 Q330 424 622 436"/>
  </svg>

  <p class="brand-name">KIVO Cosmetics</p>

  <section class="product-block">
    <p class="product-block__tagline">glam it up</p>
    <h1 class="product-block__name">Shimmer Lotion<br>Pore Shrinking</h1>
  </section>

  <p class="net-content">1 FL OZ</p>
</main>
</body>
</html>
```